Pellrow Strategies business card

I need a business card for my new strategic consulting LLC, Pellrow Strategies. We specialize in helping people who care about broadband technology and telecommunications policy, and we're based in Washington DC. I'm looking for a card that says smart, credible, future-facing and signals a high level of expertise. It's DC, so there's clearly a limit to how crazy we can go with this card, but I am looking for a design that reflects a company that is comfortable with technology, policy, and having a little bit fun. I'm uploading my logo below, and I'd like to have it be part of the card design in some fashion.
Target Market(s)
Telecommunications and technology policy professionals
Industry/Entity Type
Technology policy
Contact Information for Business Card
Name of business, my name (Colin Mabberly), email (colin@pellrowstrategies.example) , phone number (202-555-0148)phone number
Look and feel

```html
<!DOCTYPE html>
<html lang="en">
<head>
<meta charset="utf-8">
<title>Pellrow Strategies – Business Card</title>
<link rel="stylesheet" href="https://fonts.googleapis.com/css2?family=Montserrat:wght@400;500;600;700&display=swap">
<style>
  :root {
    --brand-blue: #0a56a0;
    --brand-navy: #053f7c;
    --ink: #1e2430;
    --paper: #ffffff;
    --backdrop: #e9ebee;
  }
  * { box-sizing: border-box; margin: 0; padding: 0; }
  html, body {
    width: 1200px; height: 1200px; overflow: hidden;
    background: var(--backdrop);
    font-family: "Montserrat", Arial, sans-serif;
  }
  .sheet {
    width: 1200px; height: 1200px;
    display: flex; flex-direction: column; align-items: center; justify-content: center;
    gap: 56px;
  }
  .card {
    position: relative;
    width: 900px; height: 514px;
    border-radius: 34px;
    overflow: hidden;
    box-shadow: 0 10px 30px rgba(0,0,0,.18);
  }
  .card-front { background: var(--paper); }
  .card-back { background: var(--brand-navy); display: flex; align-items: center; justify-content: center; }

  .brand-mark {
    display: flex; align-items: center; gap: 14px;
    font-weight: 700; letter-spacing: .01em;
  }
  .brand-dot { width: 22px; height: 22px; border-radius: 50%; }
  .card-front .brand-mark {
    position: absolute; top: 58px; right: 70px;
    font-size: 40px; color: var(--brand-blue);
  }
  .card-front .brand-dot { background: var(--brand-blue); }
  .card-back .brand-mark { font-size: 52px; color: var(--paper); }
  .card-back .brand-dot { background: var(--paper); width: 28px; height: 28px; }

  .corner-bands { position: absolute; inset: 0; width: 100%; height: 100%; }

  .contact { position: absolute; left: 130px; top: 240px; z-index: 1; }
  .contact-name {
    font-size: 36px; font-weight: 600; color: var(--brand-blue);
    letter-spacing: .02em; text-transform: uppercase;
  }
  .name-rule { width: 88px; height: 4px; background: var(--brand-blue); margin: 12px 0 22px; }
  .contact-line {
    display: flex; align-items: center; gap: 22px;
    font-size: 30px; font-weight: 400; color: var(--ink);
    margin-bottom: 16px;
  }
  .contact-icon { width: 34px; height: 34px; flex: none; }
</style>
</head>
<body>
<main class="sheet">
  <section class="card card-front" aria-label="Business card front">
    <svg class="corner-bands" viewBox="0 0 900 514" preserveAspectRatio="none" aria-hidden="true">
      <polygon points="0,514 0,504 710,466 710,514" fill="var(--brand-blue)"/>
      <polygon points="710,514 710,370 900,300 900,514" fill="var(--brand-blue)"/>
    </svg>

    <div class="brand-mark">
      <span class="brand-dot"></span>
      <span class="brand-name">Pellrow Strategies</span>
    </div>

    <div class="contact">
      <h1 class="contact-name">Colin Mabberly</h1>
      <div class="name-rule"></div>
      <p class="contact-line">
        <svg class="contact-icon" viewBox="0 0 24 24" aria-hidden="true">
          <path fill="var(--brand-blue)" d="M6.6 10.8a15.1 15.1 0 0 0 6.6 6.6l2.2-2.2c.3-.3.7-.4 1-.2 1.1.4 2.3.6 3.6.6.6 0 1 .4 1 1V20c0 .6-.4 1-1 1A17 17 0 0 1 3 4c0-.6.4-1 1-1h3.5c.6 0 1 .4 1 1 0 1.3.2 2.5.6 3.6.1.3 0 .7-.2 1z"/>
        </svg>
        202-555-0148
      </p>
      <p class="contact-line">
        <svg class="contact-icon" viewBox="0 0 24 24" aria-hidden="true">
          <rect x="2" y="5" width="20" height="14" fill="var(--brand-blue)"/>
          <path d="M2 5l10 8 10-8M2 19l7-7M22 19l-7-7" stroke="#fff" stroke-width="1.6" fill="none"/>
        </svg>
        colin@pellrowstrategies.example
      </p>
    </div>
  </section>

  <section class="card card-back" aria-label="Business card back">
    <div class="brand-mark">
      <span class="brand-dot"></span>
      <span class="brand-name">Pellrow Strategies</span>
    </div>
  </section>
</main>
</body>
</html>
```